Innovative Educational Technology Startup needs Business Cards!

"Campus Horizon" is an all-in-one, social profile based, online portal for Companies and Students to connect and carry out their brand ambassadorship tasks and requirements. The service allows for companies to more efficiently deploy brand ambassadorship opportunities to the millions of students actively seeking on-campus work experience.

Both educational and corporate tied into one (please keep that in mind for design purposes)
Updates

Project Deadline Extended
Reason: Need time to provide feedback to the several great designs that have been created! Thanks for the patience of one more day!

Target Market(s)

Those who get the card will more than likely be business men and working adults, but many educational instructors, professors, students, marketers, and propoective collegiate students will be the main target for these cards.

Industry/Entity Type

Business

Requirements
Must have
• Our Icon-Sized Logo (CH) must be a focus in regards to imagery.
• Color scheme must be Tiffany Blue/Black/White..(base of the card either white or black).
• www.campushorizonhub.com located somewhere on it, but not the main point of the card. (Logo is for that)
Should not have
• Childish or Tech-Only appeal.
• Basic font.
• Rather there be as little asymmetry in the card shape as possible. (curved edges is fine)

```html
<!DOCTYPE html>
<html lang="en">
<head>
<meta charset="utf-8">
<title>Campus Horizon — Business Cards</title>
<link rel="stylesheet" href="https://fonts.googleapis.com/css2?family=Jost:wght@400;500&display=swap">
<style>
  :root {
    --page-bg: #f4f4f4;
    --card-light: #eeeeee;
    --card-mid: #d9d9d9;
    --tiffany: #4fb8c2;
    --ink: #1c1c1c;
    --ink-soft: #3a3a3a;
    --ink-muted: #6a6a6a;
  }
  * { box-sizing: border-box; margin: 0; padding: 0; }
  html, body {
    width: 1200px; height: 1000px; overflow: hidden;
    background: var(--page-bg);
    font-family: "Jost", "Futura", sans-serif;
    color: var(--ink);
  }
  .canvas { position: relative; width: 1200px; height: 1000px; }

  .card {
    position: absolute; left: 250px;
    width: 700px; height: 400px;
    background: radial-gradient(ellipse at 50% 40%, var(--card-light) 0%, var(--card-mid) 100%);
    border-radius: 4px;
    box-shadow: 0 6px 18px rgba(0,0,0,0.18);
    overflow: hidden;
  }
  .card--front { top: 60px; }
  .card--back { top: 530px; }

  .card__stripe {
    position: absolute; left: 0; right: 0; bottom: 0; height: 52px;
    background: var(--ink);
    border-top: 9px solid var(--tiffany);
  }

  /* Front */
  .front-brand {
    position: absolute; left: 0; right: 0; top: 88px;
    display: flex; flex-direction: column; align-items: center;
  }
  .brand-mark {
    width: 86px; height: 86px; background: var(--tiffany);
    border-radius: 6px; margin-bottom: 22px;
  }
  .front-brand__name {
    font-size: 42px; font-weight: 400; letter-spacing: 1px;
    color: var(--ink); line-height: 1;
    padding: 0 18px 8px;
    border-bottom: 2px solid var(--ink);
  }
  .front-brand__url {
    margin-top: 10px; font-size: 17px; letter-spacing: 3px; color: var(--ink);
  }

  /* Back */
  .back-brand {
    position: absolute; left: 34px; top: 32px;
    display: flex; align-items: center; gap: 14px;
  }
  .back-brand .brand-mark { width: 54px; height: 54px; margin: 0; border-radius: 4px; }
  .back-brand__name { font-size: 30px; font-weight: 400; color: var(--ink); letter-spacing: 0.5px; }

  .holder { position: absolute; left: 34px; top: 232px; }
  .holder__name { font-size: 30px; font-weight: 500; letter-spacing: 1.5px; color: var(--ink); }
  .holder__title { font-size: 13px; color: var(--ink-muted); margin-top: 2px; }

  .contacts {
    position: absolute; right: 40px; top: 226px; list-style: none;
    font-size: 14px; letter-spacing: 1.2px; color: var(--ink-soft);
  }
  .contacts li { display: flex; align-items: center; gap: 12px; height: 22px; }
  .contacts svg { width: 13px; height: 13px; fill: var(--ink-soft); flex: none; }
</style>
</head>
<body>
<main class="canvas">

  <section class="card card--front" aria-label="Card front">
    <div class="front-brand">
      <div class="brand-mark" aria-hidden="true"></div>
      <div class="front-brand__name">Campus Horizon</div>
      <div class="front-brand__url">www.campushorizonhub.com</div>
    </div>
    <div class="card__stripe"></div>
  </section>

  <section class="card card--back" aria-label="Card back">
    <div class="back-brand">
      <div class="brand-mark" aria-hidden="true"></div>
      <div class="back-brand__name">Campus Horizon</div>
    </div>

    <div class="holder">
      <div class="holder__name">MR. DANIEL MORROW</div>
      <div class="holder__title">Marketing Manager</div>
    </div>

    <ul class="contacts">
      <li>
        <svg viewBox="0 0 16 16" aria-hidden="true"><path d="M3 1l3 3-2 2c1 2 3 4 5 5l2-2 3 3-2 3C6 14 2 10 1 3z"/></svg>
        +91 24 5518270
      </li>
      <li>
        <svg viewBox="0 0 16 16" aria-hidden="true"><path d="M4 0h8v16H4zM5.5 2v10h5V2z"/></svg>
        +91 17 4402931
      </li>
      <li>
        <svg viewBox="0 0 16 16" aria-hidden="true"><path d="M8 1l7 7h-2v7H9v-4H7v4H3V8H1z"/></svg>
        House # B-14 Lake Avenue
      </li>
      <li>
        <svg viewBox="0 0 16 16" aria-hidden="true"><path d="M8 1a7 7 0 1 0 4 12.7l-.8-1.3A5.5 5.5 0 1 1 13.5 8v1a1.3 1.3 0 0 1-2.6 0V4.5H9.6v.6A3.2 3.2 0 1 0 10.3 10.8 2.8 2.8 0 0 0 15 9V8a7 7 0 0 0-7-7zm0 9a2 2 0 1 1 0-4 2 2 0 0 1 0 4z"/></svg>
        www.campushorizonhub.com
      </li>
    </ul>

    <div class="card__stripe"></div>
  </section>

</main>
</body>
</html>
```